Life Coaching business needs a new flyer

We are an Australian business that specialises in Life Coaching, Career Coaching, Health and Wellness Coaching, Yoga and Pilates. We need a A4 double sided flyer that is full colour and folded to DL format. I have attached a couple of designs that I like and some pictures and would like the flyer to be bright yet stylish.

Life Coaching

```html
<!DOCTYPE html>
<html lang="en">
<head>
<meta charset="utf-8">
<title>Brightpath Coaching &amp; Meditation Studio – DL Flyer</title>
<link href="https://fonts.googleapis.com/css2?family=Source+Sans+3:wght@400;600;700&display=swap" rel="stylesheet">
<style>
  :root {
    --blue: #1f6fb8;
    --blue-dark: #1a5d9e;
    --green: #6ab23e;
    --text: #666666;
    --text-dark: #3a3a3a;
    --panel-light: #f3f3f3;
    --panel-sky: #d9ebf8;
    --white: #ffffff;
  }
  * { box-sizing: border-box; margin: 0; padding: 0; }
  html, body { width: 1200px; height: 872px; overflow: hidden; background: var(--white); }
  body { font-family: "Source Sans 3", Arial, sans-serif; position: relative; color: var(--text); }
  .artwork { position: absolute; inset: 0; }
  .crop-mark { stroke: #444; stroke-width: 1; }

  .testimonials { position: absolute; left: 76px; top: 78px; width: 299px; }
  .testimonials h2 { color: var(--blue); font-size: 15.5px; font-weight: 700; margin-bottom: 4px; }
  .quote { font-size: 12.6px; line-height: 16px; text-align: justify; margin-bottom: 16px; }
  .quote cite { display: block; font-style: normal; text-align: left; }

  .brand { position: absolute; display: flex; flex-direction: column; align-items: center; text-align: center; }
  .brand-dot { border-radius: 50%; background: var(--green); }
  .brand-name { color: var(--blue); font-weight: 600; letter-spacing: 0.5px; }
  .brand--middle { left: 411px; width: 376px; top: 178px; }
  .brand--middle .brand-dot { width: 64px; height: 64px; margin-bottom: 10px; }
  .brand--middle .brand-name { font-size: 18px; }
  .brand--cover { left: 800px; width: 360px; top: 62px; }
  .brand--cover .brand-dot { width: 96px; height: 96px; margin-bottom: 14px; }
  .brand--cover .brand-name { font-size: 24px; }

  .intro { position: absolute; left: 441px; width: 316px; top: 302px; text-align: center; font-size: 12.8px; line-height: 16.5px; }
  .intro p + p { margin-top: 16px; }

  .offer { position: absolute; left: 447px; top: 437px; width: 289px; height: 70px;
    border: 2px solid var(--blue); border-radius: 8px; background: var(--white);
    display: flex; align-items: center; justify-content: center; text-align: center;
    color: var(--text-dark); font-weight: 700; font-size: 13.5px; line-height: 17px; }

  .contact { position: absolute; left: 411px; width: 376px; top: 724px; text-align: center; }
  .contact .services { color: var(--blue); font-size: 11px; margin-bottom: 4px; }
  .contact .phone { color: var(--blue); font-weight: 700; font-size: 17px; display: flex; justify-content: center; align-items: center; gap: 6px; }
  .contact .email { color: var(--text-dark); font-weight: 600; font-size: 13px; margin-top: 4px; }
  .contact .web { color: var(--text-dark); font-size: 12.5px; margin-top: 5px; }

  .cover-services { position: absolute; left: 787px; width: 386px; top: 744px; text-align: center; color: var(--blue); font-weight: 700; font-size: 18px; }
  .cover-web { position: absolute; left: 787px; width: 386px; top: 780px; text-align: center; color: var(--text); font-weight: 600; font-size: 13.5px; }
</style>
</head>
<body>
<svg class="artwork" width="1200" height="872" viewBox="0 0 1200 872">
  <defs>
    <linearGradient id="leftPanel" x1="0" y1="0" x2="0" y2="1">
      <stop offset="0" stop-color="#eef4fa"/>
      <stop offset="1" stop-color="#ffffff"/>
    </linearGradient>
    <linearGradient id="middlePanel" x1="0" y1="0" x2="0" y2="1">
      <stop offset="0" stop-color="#f3f3f3"/>
      <stop offset="0.55" stop-color="#eef3f7"/>
      <stop offset="1" stop-color="#d4e8f7"/>
    </linearGradient>
    <linearGradient id="sunsetPhoto" x1="0" y1="0" x2="1" y2="1">
      <stop offset="0" stop-color="#f6d9a8"/>
      <stop offset="0.5" stop-color="#c98a5e"/>
      <stop offset="1" stop-color="#5d4a44"/>
    </linearGradient>
    <linearGradient id="convertiblePhoto" x1="0" y1="0" x2="0" y2="1">
      <stop offset="0" stop-color="#8fc8ee"/>
      <stop offset="0.55" stop-color="#cfe6f3"/>
      <stop offset="0.75" stop-color="#e873a8"/>
      <stop offset="1" stop-color="#d24f8c"/>
    </linearGradient>
    <linearGradient id="portraitPhoto" x1="0" y1="0" x2="1" y2="1">
      <stop offset="0" stop-color="#b9ad9f"/>
      <stop offset="1" stop-color="#4b3d36"/>
    </linearGradient>
  </defs>

  <g class="crop-marks">
    <line class="crop-mark" x1="0" y1="27" x2="16" y2="27"/>
    <line class="crop-mark" x1="27" y1="0" x2="27" y2="16"/>
    <line class="crop-mark" x1="1184" y1="27" x2="1200" y2="27"/>
    <line class="crop-mark" x1="1173" y1="0" x2="1173" y2="16"/>
    <line class="crop-mark" x1="0" y1="847" x2="16" y2="847"/>
    <line class="crop-mark" x1="27" y1="856" x2="27" y2="872"/>
    <line class="crop-mark" x1="1184" y1="847" x2="1200" y2="847"/>
    <line class="crop-mark" x1="1173" y1="856" x2="1173" y2="872"/>
  </g>

  <rect x="27" y="27" width="384" height="600" fill="url(#leftPanel)"/>
  <rect x="411" y="27" width="376" height="820" fill="url(#middlePanel)"/>

  <g role="img" aria-label="Photo: joyful young woman with arms raised standing in a pink convertible under a bright sky">
    <path d="M787,220 Q980,285 1173,230 L1173,640 Q980,720 787,670 Z" fill="url(#convertiblePhoto)"/>
  </g>

  <path d="M411,168 Q600,140 787,200 Q980,262 1173,208 L1173,232 Q980,292 787,228 Q600,172 411,188 Z" fill="var(--blue)"/>
  <path d="M787,228 Q980,292 1173,232 L1173,240 Q980,300 787,236 Z" fill="var(--white)"/>

  <path d="M787,662 Q980,718 1173,628 L1173,652 Q980,738 787,690 Z" fill="var(--green)"/>
  <path d="M787,690 Q980,738 1173,652 L1173,680 Q980,758 787,716 Z" fill="var(--blue)"/>
  <path d="M787,716 Q980,758 1173,680 L1173,847 L787,847 Z" fill="var(--white)"/>

  <g role="img" aria-label="Photo: group of happy friends celebrating by the coast at sunset">
    <path d="M27,610 Q200,585 411,615 L411,847 L27,847 Z" fill="url(#sunsetPhoto)"/>
  </g>
  <path d="M27,580 Q200,540 411,560 L411,585 Q220,570 27,612 Z" fill="var(--green)"/>
  <path d="M27,612 Q220,570 411,585 L411,600 Q220,592 27,640 Z" fill="var(--blue)"/>

  <circle cx="593" cy="616" r="95" fill="var(--blue)"/>
  <g role="img" aria-label="Photo: portrait of the two coaches">
    <circle cx="593" cy="616" r="88" fill="url(#portraitPhoto)"/>
  </g>
</svg>

<section class="testimonials">
  <h2>OUR HAPPY CLIENTS</h2>
  <blockquote class="quote">“I have lost 10 kilos and now have the energy to play with my kids. Thanks Mara for your support/guidance and helping me get rid of my limiting beliefs. I feel I can achieve anything now! The sky’s the limit”<cite>Jess, Mosman</cite></blockquote>
  <blockquote class="quote">“I had always wanted to start up my own café however every time it came to putting it into practice I would procrastinate and not achieve anything. I became overwhelmed with the whole process and never achieved anything. Mara put it into bite sized chunks and helped me to set small achievable goals. I am now a happy café owner.”<cite>Tara, Double Bay</cite></blockquote>
  <blockquote class="quote">“Mara has helped to change my life around in all aspects. I would have been lost without her. Thanks Mara for your professionalism, support and guidance.”<cite>Olivia, Cremorne</cite></blockquote>
  <blockquote class="quote">“I was so busy with kids, work, and my husband I lost who I was. Mara has helped me find the person I am again.”<cite>Emma, Chatswood</cite></blockquote>
</section>

<div class="brand brand--middle">
  <span class="brand-dot"></span>
  <span class="brand-name">Brightpath Studio</span>
</div>

<div class="intro">
  <p>Brightpath Coaching &amp; Meditation Studio is a professional service that can help you achieve the goals that you are looking for in Life Coaching, Meditation, and Yoga/Pilates</p>
  <p>If you are ready to take your life to the next level and would like to know more, please contact us</p>
</div>

<div class="offer">Free Introductory Life Coaching<br>Phone/Video session -20 mins<br>(To see if coaching is right for you)</div>

<div class="contact">
  <p class="services">LIFE COACHING • MEDITATION • YOGA/PILATES</p>
  <p class="phone">
    <svg width="16" height="16" viewBox="0 0 16 16" aria-hidden="true"><circle cx="8" cy="8" r="7" fill="none" stroke="currentColor" stroke-width="1.5"/><path d="M5.2,4.5 L6.6,4.3 L7.2,6 L6.4,6.7 Q7.2,8.6 9.2,9.6 L9.9,8.8 L11.6,9.4 L11.4,10.8 Q7.6,11.2 5.2,4.5 Z" fill="currentColor"/></svg>
    02 9000 4417
  </p>
  <p class="email">hello@brightpathstudio.com.au</p>
  <p class="web">www.brightpathstudio.com.au</p>
</div>

<div class="brand brand--cover">
  <span class="brand-dot"></span>
  <span class="brand-name">Brightpath Studio</span>
</div>

<p class="cover-services">Life Coaching • Meditation • Yoga/Pilates</p>
<p class="cover-web">www.brightpathstudio.com.au</p>
</body>
</html>
```